STOREFRONT LIT SIGN for The Cantera Loft

A sign advertising our music academy. This sign will be hung 10 feet above the entrance of our building and will be seen by all pedestrian and vehicle traffic on Main Street Delano.

Target Market(s)

Street passerby

Industry/Entity Type

Music Training

Font styles to use
Other font styles liked:
• Creative

Colors

Designer to choose colors to be used in the design.

Requirements
Must have
• A White Background
• Dimensions: 8 ft long x 3 ft tall
• The Cantera Loft of Delano
• Lecciones de Piano, Violin, Guitarra, Voz, Trompeta y Mas
• MUSIC ACADEMY *(This should be most prominent)
• Guitar, Voice, Trumpet and More
• (661) 478-5926
• thecanteraloft.example
Nice to have
• Graphics of a piano, or guitar, or violin or trumpet or a combination of two or more

```html
<!DOCTYPE html>
<html lang="en">
<head>
<meta charset="utf-8">
<title>The Cantera Loft – Storefront Sign</title>
<link rel="stylesheet" href="https://fonts.googleapis.com/css2?family=Fira+Sans:wght@600;700;800&family=Montserrat:wght@600;700;800&display=swap">
<style>
  :root {
    --backdrop: #4a4a4a;
    --sign-white: #ffffff;
    --sign-mist: #e7eaee;
    --navy: #0f2c62;
    --royal: #0b5c9e;
    --crimson: #931a2b;
    --ink: #141414;
    --charcoal: #3b3b3b;
    --art-grey: #5c5c5c;
  }
  * { margin: 0; padding: 0; box-sizing: border-box; }
  html, body {
    width: 1200px; height: 581px; overflow: hidden;
    background: var(--backdrop);
  }
  .sign {
    position: absolute; left: 74px; top: 74px;
    width: 1054px; height: 397px; overflow: hidden;
    background:
      linear-gradient(170deg, transparent 38%, rgba(210,215,222,.45) 52%, transparent 66%),
      linear-gradient(190deg, transparent 55%, rgba(215,220,226,.5) 68%, transparent 82%),
      linear-gradient(180deg, var(--sign-white) 0%, var(--sign-mist) 45%, var(--sign-white) 100%);
    box-shadow: 0 10px 18px rgba(0,0,0,.35);
  }
  .line { position: absolute; left: 0; width: 100%; text-align: center; white-space: nowrap; }
  .studio-name {
    top: 14px;
    font: 800 104px/1 "Fira Sans", sans-serif;
    letter-spacing: .005em;
    background: linear-gradient(90deg, var(--navy) 0%, var(--royal) 45%, var(--navy) 70%, var(--royal) 100%);
    -webkit-background-clip: text; background-clip: text; color: transparent;
  }
  .academy {
    top: 116px;
    font: 700 94px/1 "Fira Sans", sans-serif;
    letter-spacing: .09em;
    color: var(--crimson);
  }
  .lessons-es {
    top: 221px;
    font: 700 20px/1 "Montserrat", sans-serif;
    color: var(--ink);
  }
  .lessons-en {
    top: 268px;
    font: 800 38px/1 "Montserrat", sans-serif;
    color: var(--crimson);
  }
  .divider {
    position: absolute; left: 462px; top: 331px;
    width: 131px; height: 2px; background: var(--crimson);
  }
  .contact {
    position: absolute; top: 346px; left: 0; width: 100%;
    display: flex; justify-content: center; align-items: center; gap: 12px;
    font: 700 29px/1 "Montserrat", sans-serif; color: var(--charcoal);
  }
  .contact .item { display: flex; align-items: center; gap: 12px; }
  .contact .item + .item { margin-left: 14px; }
  .contact svg { width: 22px; height: 22px; flex: none; }
  .art { position: absolute; }
  .violin-art {
    left: 0; top: 133px; width: 145px; height: 264px;
    background: radial-gradient(ellipse at 55% 65%, var(--art-grey) 0%, rgba(92,92,92,.55) 45%, rgba(255,255,255,0) 75%);
  }
  .clef-art {
    left: 938px; top: 110px; width: 116px; height: 287px;
    background: radial-gradient(ellipse at 50% 50%, var(--art-grey) 0%, rgba(92,92,92,.5) 45%, rgba(255,255,255,0) 75%);
  }
</style>
</head>
<body>
  <main class="sign">
    <div class="art violin-art" role="img" aria-label="Grey violin with bow and flowing musical staff notes"></div>
    <div class="art clef-art" role="img" aria-label="Grey treble clef formed from piano keys"></div>

    <h1 class="line studio-name">THE CANTERA LOFT</h1>
    <h2 class="line academy">MUSIC ACADEMY</h2>
    <p class="line lessons-es">LECCIONES DE PIANO, VIOLIN, GUITARRA, VOZ, TROMPETA Y MAS</p>
    <p class="line lessons-en">GUITAR, VOICE, TRUMPET AND MORE</p>
    <div class="divider"></div>

    <div class="contact">
      <span class="item">
        <svg viewBox="0 0 24 24" aria-hidden="true">
          <circle cx="12" cy="12" r="12" fill="#931a2b"/>
          <path d="M8.6 6.5c.4-.3 1-.2 1.2.2l1.1 2c.2.4.1.8-.2 1.1l-.8.7c.5 1.3 1.4 2.3 2.6 2.9l.7-.8c.3-.3.8-.4 1.1-.2l2 1.1c.4.2.5.8.2 1.2l-.9 1.2c-.4.5-1 .7-1.6.5-3.2-1-5.6-3.4-6.5-6.6-.2-.6 0-1.2.5-1.6z" fill="#fff"/>
        </svg>
        (661) 478-5926
      </span>
      <span class="item">
        <svg viewBox="0 0 24 24" aria-hidden="true" fill="none" stroke="#931a2b" stroke-width="2">
          <circle cx="12" cy="12" r="10"/>
          <ellipse cx="12" cy="12" rx="4.5" ry="10"/>
          <path d="M2 12h20M4 6.5h16M4 17.5h16"/>
        </svg>
        WWW.THECANTERALOFT.EXAMPLE
      </span>
    </div>
  </main>
</body>
</html>
```